Home Loan Introducer needs logo/business cards

We need a simple but classy logo for business cards and flyers. The business is a home loan referral business that is called an Introducer. The business name is "The Pellgrove".
I was thinking very simple and straight to the point on the front with "Home Loans" the only thing on the front with a nice background colour/s.
Then on the back, "The Pellgrove"
and "Quality Customer Service"
and "Email, text or call welcome"
and then my name, email address and phone number.
Thank you for all the designs :-)
Home buyers.
Home owners.
Investors.
Loan

```html
<!DOCTYPE html>
<html lang="en">
<head>
<meta charset="utf-8">
<title>The Pellgrove – Home Loans Business Card</title>
<link rel="stylesheet" href="https://fonts.googleapis.com/css2?family=Roboto+Condensed:wght@700&display=swap">
<style>
  :root {
    --page: #ffffff;
    --card: #0a0a0a;
    --lime: #4cff00;
    --lime-soft: rgba(76, 255, 0, 0.45);
    --lime-clear: rgba(76, 255, 0, 0);
  }
  html, body {
    margin: 0;
    padding: 0;
    width: 1200px;
    height: 750px;
    overflow: hidden;
    background: var(--page);
  }
  .canvas {
    position: relative;
    width: 1200px;
    height: 750px;
  }
  .card {
    position: absolute;
    left: 291px;
    width: 592px;
    height: 304px;
    background: var(--card);
    overflow: hidden;
  }
  .card--front { top: 45px; }
  .card--back { top: 378px; }
  .card-title {
    position: absolute;
    margin: 0;
    font-family: "Roboto Condensed", "Arial Narrow", sans-serif;
    font-weight: 700;
    color: var(--lime);
    white-space: nowrap;
    line-height: 1;
  }
  .card-title--front {
    left: 123px;
    top: 125px;
    font-size: 52px;
    letter-spacing: 0.14em;
  }
  .card-title--back {
    left: 93px;
    top: 133px;
    font-size: 44px;
    letter-spacing: 0.16em;
  }
  .card-flourish {
    position: absolute;
    right: 0;
    bottom: 0;
    width: 170px;
    height: 200px;
    background: radial-gradient(ellipse 100% 100% at 100% 100%,
      var(--lime) 0%,
      var(--lime-soft) 45%,
      var(--lime-clear) 100%);
  }
</style>
</head>
<body>
  <main class="canvas">
    <section class="card card--front" aria-label="Card front">
      <h1 class="card-title card-title--front">Home Loans</h1>
    </section>
    <section class="card card--back" aria-label="Card back">
      <h2 class="card-title card-title--back">The Pellgrove</h2>
      <div class="card-flourish" role="img" aria-label="Lime green leafy scroll ornament in the bottom-right corner"></div>
    </section>
  </main>
</body>
</html>
```